Steelcrest Process Systems. Needs a Business Card Design

We need a business card design for an engineering company which supplies industrial components (pumps, compressors, mechanical seals) provides repairs and services for above mentioned equipments. We offer a uniqe engineering solutions which help our customers to increase the productivness of their manufacturings, and energy savings.

Target Market(s)

Chemical and energy plants, refineries. Food industry and private consumers in a less.

Industry/Entity Type

Business

Contact Information for Business Card

Stylish and sleek design oriented on industrial area.

Requirements
Should not have
• company name shortening

```html
<!DOCTYPE html>
<html lang="en">
<head>
<meta charset="utf-8">
<title>Steelcrest Process Systems – Business Card</title>
<link rel="stylesheet" href="https://fonts.googleapis.com/css2?family=Fira+Sans:wght@400;500;700&display=swap">
<style>
  :root {
    --stage: #2b2b2d;
    --orange: #f7a12b;
    --blue: #1a4ba8;
    --blue-deep: #133a8a;
    --red: #e8455a;
    --amber: #f5a623;
    --white: #ffffff;
    --ink-blue: #1d4aa6;
  }
  * { margin: 0; padding: 0; box-sizing: border-box; }
  html, body {
    width: 1200px; height: 950px; overflow: hidden;
    background: var(--stage);
    font-family: "Fira Sans", Arial, sans-serif;
  }
  .canvas { position: relative; width: 1200px; height: 950px; }

  .card {
    position: absolute; width: 560px; height: 320px;
    border-radius: 4px; overflow: hidden;
    box-shadow: 0 18px 40px rgba(0,0,0,.45);
  }

  /* Front */
  .card-front {
    left: 90px; top: 110px;
    background: var(--orange);
    color: var(--white);
    display: flex; flex-direction: column; align-items: center; justify-content: center;
  }
  .front-brand { display: flex; align-items: center; gap: 14px; margin-top: -10px; }
  .front-brand .dot { width: 30px; height: 30px; border-radius: 50%; background: var(--white); }
  .front-brand .name { font-size: 30px; font-weight: 500; letter-spacing: .5px; }
  .front-web {
    margin-top: 58px; font-size: 15px; letter-spacing: 6px; text-transform: uppercase;
  }

  /* Back */
  .card-back { left: 550px; top: 520px; background: var(--white); }
  .card-back .wave { position: absolute; inset: 0; }
  .back-brand {
    position: absolute; left: 34px; top: 150px;
    display: flex; align-items: center; gap: 10px;
    color: var(--ink-blue);
  }
  .back-brand .dot { width: 16px; height: 16px; border-radius: 50%; background: var(--ink-blue); }
  .back-brand .name { font-size: 19px; font-weight: 500; line-height: 1.15; }

  .contact {
    position: absolute; right: 26px; top: 26px;
    text-align: right; color: var(--white);
  }
  .contact .person { font-size: 22px; font-weight: 700; letter-spacing: .5px; }
  .contact .role { font-size: 12px; font-weight: 700; letter-spacing: 1px; margin-top: 2px; }
  .contact .address { margin-top: 44px; font-size: 13px; line-height: 1.35; padding-right: 22px; }
  .contact ul { list-style: none; margin-top: 10px; font-size: 13px; line-height: 1.45; }
  .contact li { display: flex; justify-content: flex-end; align-items: center; gap: 8px; }
  .contact li svg { width: 14px; height: 14px; fill: var(--white); flex: none; }
</style>
</head>
<body>
<main class="canvas">

  <section class="card card-front" aria-label="Card front">
    <div class="front-brand">
      <span class="dot"></span>
      <span class="name">Steelcrest Process Systems</span>
    </div>
    <p class="front-web">www.steelcrestps.com</p>
  </section>

  <section class="card card-back" aria-label="Card back">
    <svg class="wave" viewBox="0 0 560 320" preserveAspectRatio="none" aria-hidden="true">
      <path d="M225,0 C305,10 300,120 280,170 C262,220 280,295 345,320 L560,320 L560,0 Z" fill="var(--blue)"/>
      <path d="M205,0 C290,12 292,110 280,150" fill="none" stroke="var(--red)" stroke-width="4"/>
      <path d="M272,185 C262,235 285,298 338,320" fill="none" stroke="var(--amber)" stroke-width="5"/>
    </svg>

    <div class="back-brand">
      <span class="dot"></span>
      <span class="name">Steelcrest<br>Process Systems</span>
    </div>

    <div class="contact">
      <p class="person">MARCUS HALE</p>
      <p class="role">PRESIDENT</p>
      <p class="address">2170 Harbor Mill Road<br>Alder Bay, NJ 07840</p>
      <ul>
        <li>555 0148 2267
          <svg viewBox="0 0 16 16"><path d="M3 1l3 3-1.5 2a9 9 0 0 0 5.5 5.5L12 10l3 3-2 2C7 15 1 9 1 3z"/></svg></li>
        <li>555 0193 4410
          <svg viewBox="0 0 16 16"><path d="M4 0h8a1 1 0 0 1 1 1v14a1 1 0 0 1-1 1H4a1 1 0 0 1-1-1V1a1 1 0 0 1 1-1zm1 2v10h6V2zm3 11a1 1 0 1 0 0 2 1 1 0 0 0 0-2z"/></svg></li>
        <li>marcus@steelcrestps.com
          <svg viewBox="0 0 16 16"><path d="M1 3h14v10H1zm1 1.5V12h12V4.5L8 9z"/></svg></li>
        <li>www.steelcrestps.com
          <svg viewBox="0 0 16 16"><path d="M8 0a8 8 0 1 0 0 16A8 8 0 0 0 8 0zm0 1.5c.9 0 2 2 2.3 5.5H5.7C6 3.5 7.1 1.5 8 1.5zM5.7 9h4.6C10 12.5 8.9 14.5 8 14.5S6 12.5 5.7 9zM2 7a6 6 0 0 1 2.3-4.3C3.9 4 3.7 5.4 3.6 7zm10.4 0c-.1-1.6-.3-3-.7-4.3A6 6 0 0 1 14 7zM2 9h1.6c.1 1.6.3 3 .7 4.3A6 6 0 0 1 2 9zm10.4 0H14a6 6 0 0 1-2.3 4.3c.4-1.3.6-2.7.7-4.3z"/></svg></li>
      </ul>
    </div>
  </section>

</main>
</body>
</html>
```